An Agro-Processor Needs a Packaging Design

We need packaging designs for a range of dried fruits and jams with a family look. The line-up has five variants of dried fruits and five variants of jams (the designs to include front and back of the packaging). The entire range will be marketed under the 'Verdyx' brand name - please find the logo attached (the logo has a lock-up with the tagline). The packaging format for the dried fruits are resealable stand-up pouches and the jams are glass bottles - please find attached pictures of the packaging formats for reference.

Please find inspiration boards for the packaging design. Also find attached inspiration board for the design style required for the back of the dried fruit packaging.

For the dried fruit packaging, we need to develop a seal that conveys organic and sugar-free claims (please find attached example of a seal)

Target Market(s)

Organic and natural living enthusiasts who would pay a premium to get the best for them and their families

Industry/Entity Type

Food Production

Font styles to use
Sans Serif
Script

Colors

Designer to choose colors to be used in the design.

Requirements
Must have
• - The brand name 'verdyx' is inspired by the abundance of nature in Africa, it also connotes organic, natural, freshness, delicateness, airiness, sophistication and premium and therefore the design should project these values
• - The design styling to be fun, modern and 'simplistic'
• - Please find below the packaging copy for both dried fruits and jams
• DRIED FRUIT FRONT PACKAGING:
• LOGO: Verdyx - Sunshine in Every Bite
• FIVE VARIANT NAMES: Jolly Pineapple | Dreamy Mango | Breezy Banana | Cheeky Papaya | Dapper Jackfruit
• Dried
• DEVELOP A SEAL: 100% Organic | No Added Sugar (please see example attached)
• Ugandan Origin
• Net Weight: 100g
• DRIED FRUIT BACK COPY:
• Nature's best tasting fruits are also the healthiest which is why we have made it our mission to spread nature's love! Nourished by the tropical rains on the sun-drenched soils of Africa and cultivated by the caring hands of the local farmers, our organic range of dried fruits are nutrient-dense, high in fiber and rich in minerals. Enjoy them in your salads and cereals or simply relish them as a snack! They are diet-friendly if eaten in moderation and are a natural source of energy.
• VISUAL: Stack of Fruit Visual with arrows, each with the following claims (see examples attached in the inspiration boards):
• - 100% Organic
• - No Added Sugar
• - Nutrient-Dense
• - High in Fiber
• - Rich in Minerals
• INCLUDE: Nutritional Facts Table
• Ingredients: Mango - contains 100% fruit with no added sugars, preservatives, additives, colorings or flavorings.
• Reseal the pack to maintain freshness. Store in a cool and dry place.
• INCLUDE SPACE FOR: Batch Code / Expiry Date
• Barcode
• Produced by: Kelvane Food Industries, P. O. Box XXXXX, Kampala - Uganda.
• Find out more about us:
• Telephone: +XXX-XXX-XXXXXX
• Email: Info@KelvaneFoodIndustries.example
• www.Sociapage.example/Verdyx
• JAM FRONT COPY:
• FIVE VARIANT NAMES: Jolly Pineapple with a Hint of Ginger | Dreamy Mango with a Kiss of Vanilla | Breezy Banana with a Twist of Chocolate | Cheeky Papaya with a Pinch of Cardamon | Dapper Jackfruit with a Touch of Cinnamon
• Jam
• Ugandan Origin
• Net Weight: 400g
• JAM BACK COPY:
• Nature's best tasting fruits are also the healthiest which is why we have made it our mission to spread nature's love! Our range of jams come from fruits that have been nourished by the tropical rains on the sun-drenched soils of Africa and have been cultivated by the caring hands of the local farmers. We pride ourselves on making sure that the jams taste as delicious and look as natural as the perfectly ripened fruit! We then make it even better by pairing it with a hint of spice! Enjoy them in your breakfast or use them as a filling in baking.
• Ingredients: Mango, citric acid, sugar, pectin, vanilla
• Barcode
• Find out more about us:

```html
<!DOCTYPE html>
<html lang="en">
<head>
<meta charset="utf-8">
<title>Verdyx Dreamy Mango – Dried Fruit Pouch Front</title>
<link href="https://fonts.googleapis.com/css2?family=Amatic+SC:wght@700&family=Baloo+2:wght@500;600&family=Kaushan+Script&display=swap" rel="stylesheet">
<style>
  :root{
    --canvas:#ffffff;
    --pouch-light:#f7f8f6;
    --pouch-mid:#e4e7e3;
    --leaf-light:#a9d44a;
    --leaf-dark:#4f8f2a;
    --mango-orange:#f0a02a;
    --label-lime:#b6dc3c;
    --label-pale:#f2f7dc;
    --brand-brown:#4a3328;
    --tag-red:#e0493a;
    --title-orange:#f07a1a;
    --seal-green:#1d6b3a;
    --band-green:#1f6a2c;
    --band-deep:#14501f;
    --white:#ffffff;
  }
  html,body{margin:0;padding:0;overflow:hidden;}
  body{width:1200px;height:1200px;background:var(--canvas);position:relative;font-family:"Baloo 2",sans-serif;}
  .pouch{
    position:absolute;left:350px;top:250px;width:500px;height:703px;overflow:hidden;
    background:linear-gradient(90deg,var(--pouch-mid) 0%,var(--pouch-light) 18%,var(--white) 50%,var(--pouch-light) 82%,var(--pouch-mid) 100%);
  }
  .top-art{
    position:absolute;left:0;top:0;width:500px;height:230px;
    background:
      radial-gradient(ellipse 120px 130px at 250px 150px,var(--mango-orange) 0%,#e89a2a 70%,transparent 72%),
      linear-gradient(180deg,var(--leaf-light) 0%,#8cc23e 45%,rgba(169,212,74,0.35) 80%,rgba(255,255,255,0) 100%);
  }
  .label-panel{
    position:absolute;left:90px;top:176px;width:317px;height:440px;border-radius:22px 22px 0 0;
    background:radial-gradient(ellipse 190px 230px at 50% 48%,var(--label-pale) 0%,#dcee9a 50%,var(--label-lime) 100%);
  }
  .brand{position:absolute;left:90px;top:206px;width:317px;text-align:center;}
  .brand-name{font-family:"Baloo 2",sans-serif;font-weight:600;font-size:46px;line-height:1;color:var(--brand-brown);letter-spacing:1px;}
  .brand-tagline{font-family:"Baloo 2",sans-serif;font-weight:500;font-size:14px;color:var(--tag-red);margin-top:2px;}
  .variant{position:absolute;left:90px;width:317px;text-align:center;font-family:"Amatic SC",sans-serif;font-weight:700;line-height:1;}
  .variant-line1{top:284px;font-size:62px;color:var(--brand-brown);letter-spacing:2px;}
  .variant-line2{top:332px;font-size:62px;color:var(--title-orange);letter-spacing:3px;}
  .dried{position:absolute;left:136px;top:408px;font-family:"Kaushan Script",cursive;font-size:42px;color:var(--brand-brown);transform:rotate(-8deg);}
  .dried-underline{position:absolute;left:134px;top:460px;}
  .seal{position:absolute;left:270px;top:398px;width:86px;height:86px;}
  .fruit-pile{
    position:absolute;left:150px;top:476px;width:206px;height:124px;border-radius:40% 45% 35% 40%;
    background:radial-gradient(ellipse at 50% 45%,#f4c23a 0%,#e9a52a 60%,rgba(233,165,42,0.4) 85%,rgba(233,165,42,0) 100%);
  }
  .bottom-band{position:absolute;left:0;top:520px;width:500px;height:183px;}
  .origin{position:absolute;left:0;width:500px;top:622px;text-align:center;font-family:"Amatic SC",sans-serif;font-weight:700;font-size:14px;color:var(--white);letter-spacing:1px;}
  .weight{position:absolute;left:0;width:500px;top:640px;text-align:center;font-family:"Amatic SC",sans-serif;font-weight:700;font-size:36px;color:var(--white);}
</style>
</head>
<body>
  <main class="pouch">
    <div class="top-art" role="img" aria-label="Ripe mango hanging among green mango leaves"></div>
    <div class="label-panel"></div>

    <div class="brand">
      <div class="brand-name">verdyx</div>
      <div class="brand-tagline">Sunshine in Every Bite</div>
    </div>

    <h1 class="variant variant-line1" style="margin:0">DREAMY</h1>
    <div class="variant variant-line2">MANGO</div>

    <div class="dried">Dried</div>
    <svg class="dried-underline" width="110" height="24" viewBox="0 0 110 24"><path d="M4 20 Q50 4 106 2" stroke="var(--brand-brown)" stroke-width="2.5" fill="none" stroke-linecap="round"/></svg>

    <svg class="seal" viewBox="0 0 86 86" aria-label="100% Organic, No Added Sugar seal">
      <defs>
        <path id="sealTop" d="M15 43 A28 28 0 0 1 71 43"/>
        <path id="sealBottom" d="M13 43 A30 30 0 0 0 73 43"/>
      </defs>
      <circle cx="43" cy="43" r="42" fill="var(--seal-green)"/>
      <circle cx="43" cy="43" r="38" fill="none" stroke="var(--white)" stroke-width="1"/>
      <text font-family="Baloo 2, sans-serif" font-size="8" font-weight="600" fill="var(--white)" letter-spacing="0.6"><textPath href="#sealTop" startOffset="50%" text-anchor="middle">100% ORGANIC</textPath></text>
      <text font-family="Baloo 2, sans-serif" font-size="8" font-weight="600" fill="var(--white)" letter-spacing="0.6" dy="6"><textPath href="#sealBottom" startOffset="50%" text-anchor="middle">NO ADDED SUGAR</textPath></text>
      <circle cx="43" cy="44" r="13" fill="#e6efd9" role="img" aria-label="Small pineapple drawing"/>
    </svg>

    <div class="fruit-pile" role="img" aria-label="Pile of golden dried mango slices"></div>

    <svg class="bottom-band" viewBox="0 0 500 183" preserveAspectRatio="none">
      <path d="M0 20 Q250 110 500 0 L500 183 L0 183 Z" fill="var(--band-green)"/>
      <path d="M0 150 Q250 175 500 145 L500 183 L0 183 Z" fill="var(--band-deep)" opacity="0.35"/>
    </svg>

    <div class="origin">UGANDAN ORIGIN</div>
    <div class="weight">100g</div>
  </main>
</body>
</html>
```